Property portal page designs

We are looking for some webpage designs (mock-ups) for a new property portal - Nestorix.com.

We are looking for at least 3 page designs based on the following 3 pages of Havrik:

1. Homepage design based on www.havrik.example
2. Search results page based on http://www.havrik.example/homes/
3. Full details page based on http://www.havrik.example/homedetails/B-7-Tovel-CA-48213/3917460528_hvid/ for example.

We want all three page designs to incorporate a new look and feel and colour palette for nestorix.com - examples of the logo for nestorix are attached.

The pages need to also incorporate what the rolls over will look like - especially when you roll over the properties in the search results page (page 2 above).

Hi there - i would like the design to be as close the havrik.example page designs as possible - but using the nestorix logo and colour scheme instead of the havrik.example logo and colour scheme. Again - I am looking for 3 page designs - 1. home page 2. Summary details, 3. Full details. Please also include how the roll-overs will appear (i.e. on the summary details, when you roll-over a property, the pop-up screen need to be included in the design etc). Thanks

```html
<!DOCTYPE html>
<html lang="en">
<head>
<meta charset="utf-8">
<title>Nestorix – Find your home</title>
<link rel="stylesheet" href="https://fonts.googleapis.com/css2?family=Arimo:wght@400;700&display=swap">
<style>
  :root{
    --canvas:#e3e1e1;
    --page:#ffffff;
    --header:#efefef;
    --footer:#eeeeee;
    --rule:#d6d6d6;
    --ink:#333333;
    --muted:#777777;
    --soft:#8a8a8a;
    --link:#3b6fc4;
    --brand:#2bab8a;
    --overlay:rgba(20,22,26,.72);
  }
  *{box-sizing:border-box;margin:0;padding:0}
  html,body{width:1200px;height:1000px;overflow:hidden}
  body{background:var(--canvas);font-family:"Arimo",Arial,sans-serif;color:var(--ink);position:relative}
  .page{position:absolute;left:275px;top:0;width:617px;height:1000px;background:var(--page)}
  .abs{position:absolute}
  a{color:inherit;text-decoration:none}

  /* header */
  .site-header{left:0;top:0;width:617px;height:40px;background:var(--header);border-bottom:1px solid #dcdcdc}
  .brand{left:46px;top:14px;display:flex;align-items:center;gap:3px;font-size:7.5px;font-weight:700;color:var(--brand);white-space:nowrap}
  .brand-dot{width:10px;height:10px;border-radius:50%;background:var(--brand)}
  .main-nav{left:90px;top:15px;display:flex;gap:11px;font-size:7.3px;color:#222;white-space:nowrap}
  .user-nav{left:452px;top:15px;display:flex;align-items:center;gap:5px;font-size:7.3px;color:#222}
  .user-nav .u{text-decoration:underline}
  .help{width:10px;height:10px;border-radius:50%;background:#111;color:#fff;font-size:7px;font-weight:700;text-align:center;line-height:10px;margin-left:6px}

  /* hero */
  .hero{left:0;top:40px;width:617px;height:278px;
    background:linear-gradient(180deg,#6ea6d9 0%,#a9cbea 30%,#c9c3b8 52%,#8e8172 70%,#4f6a3a 86%,#3c5a2c 100%)}
  .hero-arrow{top:112px;color:#fff;font-size:44px;font-weight:400;line-height:1}
  .search-box{left:170px;top:80px;width:280px;height:108px;background:var(--overlay)}
  .search-brand{left:17px;top:13px;color:#fff;font-size:14px;font-weight:700}
  .search-title{left:124px;top:12px;color:#fff;font-size:19px;font-weight:700}
  .tabs{left:17px;top:44px;display:flex;gap:16px;font-size:8px;font-weight:700;color:#fff}
  .tab{display:flex;align-items:center;gap:4px}
  .search-field{left:15px;top:71px;width:225px;height:25px;background:#fff;font-size:7.5px;color:#9a9a9a;padding:8px 8px}
  .search-btn{left:240px;top:71px;width:28px;height:25px;background:var(--brand)}

  /* reasons */
  .section-title{width:617px;text-align:center;color:var(--muted);font-size:16.5px}
  .section-sub{width:617px;text-align:center;color:var(--muted);font-size:10px}
  .reason h3,.tool h3{font-size:10px;font-weight:400;color:#222;margin-bottom:6px}
  .reason p,.tool p,.feature p{font-size:6.3px;line-height:11px;color:#444;width:140px}
  .reason{top:472px}
  .photo{border:1px solid #ccc}
  .listing-card{left:262px;top:400px;width:116px;height:40px;background:#fff;border:1px solid #cfcfcf;border-radius:3px;box-shadow:0 2px 3px rgba(0,0,0,.18)}
  .listing-card .thumb{left:3px;top:3px;width:33px;height:30px;background:linear-gradient(#9cc1e2,#c9b79b 60%,#6f8d4c)}
  .listing-card .addr{left:40px;top:6px;font-size:7.5px;font-weight:700;color:#2d66b3}
  .listing-card .status{left:40px;top:17px;font-size:6.8px;font-weight:700;display:flex;align-items:center;gap:2px}
  .listing-card .status i{width:5px;height:5px;border-radius:50%;background:#d0232a;display:inline-block}
  .listing-card .value{left:40px;top:27px;font-size:6.5px}
  .divider{left:0;width:617px;height:1px;background:var(--rule)}

  /* tools */
  .feature-frame{left:57px;top:573px;width:214px;height:143px;border:1px solid #cfcfcf;padding:3px;box-shadow:0 1px 2px rgba(0,0,0,.12)}
  .feature-frame div{width:100%;height:100%;background:linear-gradient(90deg,#d6d8da,#eef0f1 45%,#b8b4ad 70%,#dadcdd)}
  .feature{left:58px;top:725px}
  .feature h3{font-size:10px;font-weight:400;color:#222;margin-bottom:6px}
  .feature p{width:215px}
  .more{font-size:6.3px;color:var(--link);display:block}
  .tool-thumb{left:295px;width:71px;border:1px solid #cfcfcf;padding:3px}
  .tool{left:393px}
  .tool p{width:180px}

  /* footer */
  .footer-dir{left:0;top:783px;width:617px;height:167px;background:var(--footer)}
  .dir-col{top:10px}
  .dir-col h4{font-size:9.5px;font-weight:400;color:#222;margin-bottom:7px}
  .dir-col li{list-style:none;font-size:6.6px;color:#444;line-height:12.8px}
  .dir-col .more{margin-top:1px}
  .footer-links{left:0;top:950px;width:617px;height:23px;background:var(--footer);border-top:1px solid var(--rule);border-bottom:1px solid var(--rule)}
  .footer-links ul{display:flex;justify-content:center;gap:16px;list-style:none;font-size:6.6px;color:var(--link);padding-top:6px}
  .footer-base{left:0;top:973px;width:617px;height:27px;background:var(--footer);font-size:6.6px;color:#888}
  .follow{left:384px;top:7px;display:flex;align-items:center;gap:6px;color:#222;font-size:9px}
  .follow i{display:inline-block;width:9px;height:9px;border-radius:50%;background:#333}
</style>
</head>
<body>
<div class="page">

  <header class="site-header abs">
    <div class="brand abs"><span class="brand-dot"></span>Nestorix</div>
    <nav class="main-nav abs">
      <a>Homes</a><a>Rentals</a><a>Mortgages</a><a>Agents</a><a>Advice</a><a>Local</a><a>Home Design</a><a>More ▾</a>
    </nav>
    <div class="user-nav abs">
      <a>Advertise</a>
      <svg width="9" height="9" viewBox="0 0 10 10" style="margin-left:8px"><circle cx="5" cy="3" r="2.4" fill="#333"/><path d="M0.5 10c0-3 2-4.5 4.5-4.5S9.5 7 9.5 10z" fill="#333"/></svg>
      <a class="u">Sign in</a><span>or</span><a class="u">Join</a>
      <span class="help">?</span>
    </div>
  </header>

  <section class="hero abs" role="img" aria-label="Photo of a large white two-storey house with wrap-around porch under a blue sky">
    <span class="hero-arrow abs" style="left:20px">❮</span>
    <span class="hero-arrow abs" style="left:578px">❯</span>
    <div class="search-box abs">
      <div class="search-brand abs">Nestorix.com</div>
      <div class="search-title abs">Find your home</div>
      <div class="tabs abs">
        <span class="tab"><svg width="11" height="10" viewBox="0 0 11 10"><path d="M5.5 0L11 5H9.3V10H1.7V5H0z" fill="#e0262b"/></svg>For Sale</span>
        <span class="tab"><svg width="11" height="10" viewBox="0 0 11 10"><path d="M5.5 0L11 5H9.3V10H1.7V5H0z" fill="#8b3fc2"/></svg>For Rent</span>
        <span class="tab"><svg width="11" height="10" viewBox="0 0 11 10"><path d="M5.5 0L11 5H9.3V10H1.7V5H0z" fill="#2a9fd6"/></svg>Pre-market</span>
        <span class="tab"><svg width="11" height="10" viewBox="0 0 11 10"><path d="M5.5 0L11 5H9.3V10H1.7V5H0z" fill="#b9b9b9"/></svg>Nestorix</span>
      </div>
      <div class="search-field abs">Search for an Adress, Neighborhood, City or Zip</div>
      <div class="search-btn abs">
        <svg width="28" height="25" viewBox="0 0 28 25"><circle cx="12.5" cy="10.5" r="5" fill="none" stroke="#fff" stroke-width="2.2"/><path d="M16 14l5 5" stroke="#fff" stroke-width="3" stroke-linecap="round"/></svg>
      </div>
    </div>
  </section>

  <h2 class="section-title abs" style="top:329px;font-weight:400">Why shop for a home on Nestorix?</h2>
  <p class="section-sub abs" style="top:349px">Here are 3 big reasons...</p>

  <div class="photo abs" role="img" aria-label="Stack of house photos including a backyard pool" style="left:82px;top:398px;width:108px;height:64px;background:linear-gradient(135deg,#8fb0cf,#5f8fb8 40%,#6fb5d4 65%,#c9c2b0);border:3px solid #fff;box-shadow:0 1px 3px rgba(0,0,0,.3)"></div>
  <div class="reason abs" style="left:80px">
    <h3>1 million more listings</h3>
    <p>Lorem Ipsum is simply dummy text of the printing and typesetting industry. Lorem Ipsum has been the industry's standard dummy text ever since the 1500s, when an unknown printer took</p>
  </div>

  <div class="listing-card abs">
    <div class="thumb abs" role="img" aria-label="Small photo of a house"></div>
    <div class="addr abs">1231 Oak Way</div>
    <div class="status abs"><i></i>Coming Soon</div>
    <div class="value abs">Valuemark $243,000</div>
  </div>
  <div class="reason abs" style="left:262px">
    <h3>Browse hidden inventory</h3>
    <p>Lorem Ipsum is simply dummy text of the printing and typesetting industry. Lorem Ipsum has been the industry's standard dummy text ever since the 1500s, when an unknown printer took</p>
  </div>

  <div class="abs" role="img" aria-label="Round aerial map of homes with price markers" style="left:457px;top:398px;width:62px;height:62px;border-radius:50%;background:radial-gradient(circle,#8f9a86,#5c6a55);border:2px solid #e6e6e6"></div>
  <div class="reason abs" style="left:424px">
    <h3>Nestorix values on all homes</h3>
    <p>Lorem Ipsum is simply dummy text of the printing and typesetting industry. Lorem Ipsum has been the industry's standard dummy text ever since the 1500s, when an unknown printer took</p>
  </div>

  <div class="divider abs" style="top:542px"></div>
  <h2 class="section-title abs" style="top:549px;font-size:15.5px;font-weight:400;color:var(--soft)">See more valuable real estate tools and info</h2>

  <div class="feature-frame abs"><div role="img" aria-label="Bright living room interior with white armchairs"></div></div>
  <div class="feature abs">
    <h3>Home design ideas on Havrik Digs</h3>
    <p>Browse more than 1,000,000 photos of kitchens, bathrooms, outdoor spaces and more – organized by space, style, cost and color.</p>
    <a class="more">Get inspired now</a>
  </div>

  <div class="tool-thumb abs" style="top:574px;height:48px"><div role="img" aria-label="Photo of a single-family home" style="width:100%;height:100%;background:linear-gradient(#8db8e0,#b7c7d6 55%,#6f8a55)"></div></div>
  <div class="tool abs" style="top:572px">
    <h3>Los Angeles homes for sale</h3>
    <p>Shop for single-family homes, condos, townhomes – even homes not yet on the market, such as pre-foreclosures.</p>
    <a class="more">See more homes</a>
  </div>

  <div class="tool-thumb abs" style="top:633px;height:52px">
    <svg width="63" height="44" viewBox="0 0 63 44"><rect width="63" height="44" fill="#3f7a2a"/><rect x="20" y="10" width="22" height="22" fill="none" stroke="#fff" stroke-width="3"/><path d="M25 20l5 6 14-16" fill="none" stroke="#fff" stroke-width="4"/></svg>
  </div>
  <div class="tool abs" style="top:632px">
    <h3>Havrik Mortgages</h3>
    <p>Shop for single-family homes, condos, townhomes – even homes not yet on the market, such as pre-foreclosures.</p>
    <a class="more">See more homes</a>
  </div>

  <div class="tool-thumb abs" style="top:699px;height:51px"><div role="img" aria-label="Phone and tablet showing the mobile app" style="width:100%;height:100%;background:linear-gradient(135deg,#2c3b55,#4b6fa3 50%,#c99a5c)"></div></div>
  <div class="tool abs" style="top:699px">
    <h3>Havrik Mobile</h3>
    <p>Shop for single-family homes, condos, townhomes – even homes not yet on the market, such as pre-foreclosures.</p>
    <a class="more">See more homes</a>
  </div>

  <footer>
    <div class="footer-dir abs">
      <div class="dir-col abs" style="left:63px"><h4>Real Estate</h4><ul><li>Austin</li><li>Boston</li><li>Charlotte</li><li>Colorado</li><li>Colorado Springs</li><li>Columbus</li><li>Denver</li><li>El Paso</li><li>Florida</li></ul><a class="more">Show More</a></div>
      <div class="dir-col abs" style="left:187px"><h4>Apartments</h4><ul><li>Atlanta</li><li>Austin</li><li>Baltimore</li><li>Boston</li><li>Charlotte</li><li>Chicago</li><li>Dallas</li><li>Denver</li><li>Houston</li></ul><a class="more">Show More</a></div>
      <div class="dir-col abs" style="left:323px"><h4>Houses for Rent</h4><ul><li>Austin</li><li>Boston</li><li>Charlotte</li><li>Columbus</li><li>Fort Worth</li><li>Fresno</li><li>Indianapolis</li><li>Jacksonville</li><li>Las Vegas</li></ul><a class="more">Show More</a></div>
      <div class="dir-col abs" style="left:456px"><h4>Mortgage Rates</h4><ul><li>Alabama</li><li>Arizona</li><li>California</li><li>Colorado</li><li>Florida</li><li>Georgia</li><li>Illinois</li><li>Indiana</li><li>Maryland</li></ul><a class="more">Show More</a></div>
    </div>
    <nav class="footer-links abs">
      <ul><li>About</li><li>Valuemarks</li><li>Jobs</li><li>Help</li><li>Advertise</li><li>Terms of Use &amp; Privacy Policy</li><li>Ad Choice</li><li>Blog</li><li>Mobile</li></ul>
    </nav>
    <div class="footer-base abs">
      <span class="abs" style="left:168px;top:10px">Nestorix Real Estate Network</span>
      <span class="abs" style="left:293px;top:10px">© 2014 Nestorix</span>
      <div class="follow abs">Follow us <i style="margin-left:8px"></i><i></i><i></i></div>
    </div>
  </footer>

</div>
</body>
</html>
```